The Hollender House Brochure - A Real Estate Sales Brochure

I am a areal estate agent. This Brochure is for the marketing and sale of a historic home in an urban core, nationally recognized historic district. The community this home is located in, is Historic Maplecrest in Jacksonville Florida. This community borders the city core and provides quick and easy access to the heart of Jacksonville and the downtown scene.

The type of people who live in Historic Maplecrest are diverse. Virtually every race, religion and socio economic class are represented in this community. We want to develop a brochure that appeals to an urban hipster, younger buyer.
Updates

Target Market(s)

Younger home buyers who want to live close to the urban core of a metropolitan area. Ages 25 - 45 with annual income of $75,000 +

Industry/Entity Type

Real Estate

Font styles to use
Sans Serif

Requirements
Must have
• Four page brochure.
Nice to have
• Sample copy provided below:
• WOW!! The 3,288 sf Grand Dame of the Maplecrest Historic District. This Vintage home has been completely renovated. Updated wiring, plumbing, blown in insulation, Vorlex tankless gas hot water heaters, newer windows and HVAC. Also features new exterior paint, interior paint, lighting, crisp new kitchen with stainless appliances. This spacious property provides lots of living options. Four bedrooms, four baths, two kitchens, four living areas and four gas fireplaces. Main home is approx. 2,400 sf with an additional one bedroom, one bath 900 sf apartment. Keep the apartment for visiting guests or rent it and defray your monthly housing cost. On the best Street in Historic Maplecrest, this home is literally steps away from beautiful Brenner Park and downtown Jacksonville. Convenience, comfort and style. This is home!

```html
<!DOCTYPE html>
<html lang="en">
<head>
<meta charset="utf-8">
<title>The Hollender House Brochure</title>
<link href="https://fonts.googleapis.com/css2?family=Lato:wght@400;700&family=Roboto+Condensed:wght@700&display=swap" rel="stylesheet">
<style>
  :root {
    --backdrop: #8a5a36;
    --paper: #ffffff;
    --ink: #1e1e1e;
    --blue: #1260b8;
    --blue-deep: #0b4c9c;
    --sky: #3aa6dc;
    --cream: #fbefc4;
    --yellow: #f3c51e;
    --yellow-light: #f8dc5c;
    --black: #111111;
  }
  * { margin: 0; padding: 0; box-sizing: border-box; }
  html, body { width: 1200px; height: 907px; overflow: hidden; }
  body { background: var(--backdrop); font-family: "Lato", sans-serif; position: relative; }

  .spread { position: absolute; left: 96px; top: 75px; width: 1045px; height: 745px; box-shadow: 0 4px 14px rgba(0,0,0,.45); }
  .page { position: absolute; top: 0; width: 523px; height: 745px; overflow: hidden; }
  .page--inside { left: 0; background: linear-gradient(90deg, #ffffff 70%, #ececec 100%); }
  .page--cover { left: 523px; width: 522px; background: linear-gradient(180deg, var(--yellow-light), var(--yellow)); }
  .page-art { position: absolute; inset: 0; }

  .section-title { position: absolute; left: 0; width: 100%; text-align: center; font-weight: 700; font-size: 22px; }
  .section-title::before, .section-title::after { content: ""; display: inline-block; width: 110px; height: 3px; vertical-align: middle; margin: 0 10px; background: linear-gradient(90deg, transparent, var(--sky), transparent); }
  .about-title { top: 31px; color: var(--ink); }
  .about-copy { position: absolute; left: 32px; width: 467px; top: 64px; font-size: 14.6px; line-height: 19px; color: var(--ink); text-align: justify; }

  .features-title { top: 299px; color: #fff; }
  .feature-list { position: absolute; left: 32px; width: 450px; top: 337px; list-style: none; color: #fff; font-size: 14.6px; line-height: 18.6px; }
  .feature-list li { position: relative; padding-left: 20px; margin-bottom: 8px; }
  .feature-list li::before { content: ""; position: absolute; left: 1px; top: 6px; width: 8px; height: 8px; border-radius: 50%; background: var(--yellow); }

  .contact { position: absolute; left: 154px; width: 234px; top: 679px; text-align: center; font-size: 12.5px; line-height: 17px; color: var(--ink); }
  .contact svg { width: 9px; height: 9px; vertical-align: -1px; margin-right: 4px; }

  .house-photo { position: absolute; left: 0; top: 0; width: 522px; height: 325px; background: linear-gradient(180deg, #3f78d8 0%, #8ab6ea 30%, #b7c3a6 55%, #7e9a62 80%, #c9c2b3 100%); }
  .room { position: absolute; border-radius: 50%; border: 4px solid #fff; box-shadow: 0 0 0 3px var(--blue-deep), 0 3px 8px rgba(0,0,0,.4); }
  .room--bath { left: 20px; top: 285px; width: 116px; height: 116px; background: radial-gradient(circle at 50% 35%, #f2f2f2, #a33 75%, #777); }
  .room--bedroom { left: 160px; top: 278px; width: 192px; height: 192px; background: linear-gradient(180deg, #e9e7d9 0%, #c8d27a 45%, #b0622e 75%, #7a3a1a 100%); }
  .room--living { left: 365px; top: 283px; width: 124px; height: 124px; background: linear-gradient(180deg, #f1e6a6 0%, #d4c16e 60%, #333 100%); }

  .cover-title { position: absolute; left: 0; width: 100%; top: 496px; text-align: center; font-family: "Roboto Condensed", sans-serif; font-weight: 700; font-size: 46px; color: var(--black); letter-spacing: .3px; }
  .cover-subtitle { position: absolute; left: 0; width: 100%; top: 565px; text-align: center; font-size: 24.5px; color: var(--black); }
  .cover-url { position: absolute; left: 0; width: 100%; top: 678px; text-align: center; font-size: 21px; color: var(--yellow); }
</style>
</head>
<body>
<main class="spread">
  <section class="page page--inside">
    <svg class="page-art" viewBox="0 0 523 745" aria-hidden="true">
      <defs>
        <linearGradient id="blueFill" x1="0" y1="0" x2="0" y2="1">
          <stop offset="0" stop-color="#1a6fc7"/><stop offset="1" stop-color="#0b4c9c"/>
        </linearGradient>
      </defs>
      <path d="M0,318 Q250,225 523,262 L523,745 L0,745Z" fill="var(--cream)"/>
      <path d="M0,342 Q250,255 523,282 L523,745 L0,745Z" fill="url(#blueFill)"/>
      <path d="M0,652 Q80,712 260,724 Q420,734 523,682 L523,745 L0,745Z" fill="var(--sky)"/>
      <path d="M0,640 Q80,702 260,714 Q420,724 523,670" fill="none" stroke="#fff" stroke-width="6"/>
      <path d="M0,630 Q80,692 260,704 Q420,714 523,660" fill="none" stroke="var(--black)" stroke-width="7"/>
      <ellipse cx="271" cy="765" rx="120" ry="88" fill="var(--yellow)"/>
    </svg>
    <h2 class="section-title about-title">About Us</h2>
    <p class="about-copy">Lorem ipsum dolor sit amet, consectetuer adipiscing elit. Aenean commodo ligula eget dolor. Aenean massa. Cum sociis natoque penatibus et magnis dis parturient montes, nascetur ridiculus mus. Donec quam felis, ultricies nec, pellentesque eu, pretium quis, sem. Nulla consequat massa quis enim. Donec pede justo, fringilla vel, aliquet nec, vulputate eget, arcu. In enim justo, rhoncus ut, imperdiet a, venenatis vitae, justo. Nullam dictum felis eu pede mollis pretium. Integer tincidunt. Cras dapibus.Vivamus elementum semper nisi. Aenean vulputate eleifend tellus. Aenean leo ligula, porttitor eu, consequat vitae.</p>

    <h2 class="section-title features-title">Features of Apartment</h2>
    <ul class="feature-list">
      <li>The 3,288 sf Grand Dame of the Maplecrest Historic District.</li>
      <li>This Vintage home has been completely renovated. Updated wiring, plumbing, blown in insulation, Vorlex tankless gas hot water heaters, newer windows and HVAC.</li>
      <li>Also features new exterior paint, interior paint, lighting, crisp new kitchen with stainless appliances.</li>
      <li>This spacious property provides lots of living options. Four berooms, four baths, two kitchens, four living areas and four gas fireplaces.</li>
      <li>Main home is approx. 2,400 sf with an additional one bedroom, one bath 900 sf apartment. Keep the apartment for visiting guests or rent it and defray your monthly housing cost. On the best Street in Historic Maplecrest, this home is literally steps away from beautiful Brenner Park and downtown Jacksonville. Convenience, comfort and style. This is home!</li>
    </ul>

    <address class="contact">
      <div><svg viewBox="0 0 10 10"><path d="M2,0 L4,2.5 L3,3.8 Q4.5,6 6.2,7 L7.5,6 L10,8 L8.5,10 Q3,9 0,1.5Z" fill="#222"/></svg>0123456789</div>
      <div><svg viewBox="0 0 10 10"><rect x="0" y="2" width="10" height="7" fill="#222"/><path d="M0,2 L5,6 L10,2" fill="none" stroke="#f3c51e" stroke-width="1"/></svg>info@hollenderhomes.com</div>
    </address>
  </section>

  <section class="page page--cover">
    <div class="house-photo" role="img" aria-label="Photo of the two-storey historic green house with wide porches on a sunny street"></div>
    <svg class="page-art" viewBox="0 0 522 745" aria-hidden="true">
      <path d="M0,312 Q260,338 522,268 L522,296 Q260,365 0,340Z" fill="var(--black)"/>
      <path d="M0,660 Q300,585 522,625 L522,745 L0,745Z" fill="var(--black)"/>
      <path d="M0,672 Q300,598 522,637 L522,745 L0,745Z" fill="#fff"/>
      <path d="M0,680 Q300,608 522,647 L522,745 L0,745Z" fill="var(--sky)"/>
      <path d="M0,690 Q300,625 522,672 L522,745 L0,745Z" fill="var(--blue)"/>
    </svg>
    <div class="room room--bath" role="img" aria-label="Photo of a bathroom with red walls and a white window"></div>
    <div class="room room--bedroom" role="img" aria-label="Photo of a green bedroom with wooden floor and a red flower wall decal"></div>
    <div class="room room--living" role="img" aria-label="Photo of a yellow living room with fireplace and checkered floor"></div>
    <h1 class="cover-title">The Hollender House</h1>
    <p class="cover-subtitle">HISTORIC HOME IN AN URBAN CORE</p>
    <p class="cover-url">www.yourcompany.com</p>
  </section>
</main>
</body>
</html>
```